Parity Skills Forum needs a brochure to attract participants to its trainings

We need a flyer for our EU-funded project called " Parity Skills Forum" and it aims at increasing and developing skills of researchers and university staff members who are implementing measures towards gender equality in their institutions through our offered training programs. The final design should communicate gender equality for Research and Innovation centres and universities. This flyer will be distributed during conferences and events to our audience (mainly gender experts, researchers, administrative staff of universities, etc.) in order to provide the basic information about the project and options to get involved in the different trainings. We are attaching files to provide you with the concrete information on our requirements:- PS Forum flyer content.ppt: includes the content we would like to include in the flyer. There is also the URL to the project website and the different social media channels. - Project logo.zip: the project logo and guidelines as we would like to use colors that belong to the project logo color range. - Partners' logos.zip: Logos that will be included- EU flag: You can download different resolution files of the flag here: https://unionvexa.org/about-union/emblems/banner_en -Regarding the images or graphics that you may include in the brochure we wouldn’t like to propose any because we do not want to limitate your imagination.

As it was not mentioned and we received a lot of questions about it, we prefer the flyer to be double-sided and in A5

Font styles to use
Serif
Sans Serif

Colors

Designer to choose colors to be used in the design.

Requirements
Nice to have
• At least 4 pages
Should not have
• We would not like to see as dominant colours the classic blue and pink.

```html
<!DOCTYPE html>
<html lang="en">
<head>
<meta charset="utf-8">
<title>Parity Skills Forum – Flyer</title>
<link href="https://fonts.googleapis.com/css2?family=Montserrat:wght@700;800&family=Roboto+Condensed:wght@700&family=Roboto:wght@400;500&display=swap" rel="stylesheet">
<style>
:root{
  --magenta:#c0245e;
  --magenta-dark:#9c1a4b;
  --teal:#14b3c6;
  --ink:#30363b;
  --text:#3c4247;
  --panel:#efefef;
  --paper:#ffffff;
  --backdrop:#d5d5d5;
}
*{margin:0;padding:0;box-sizing:border-box}
html,body{width:1200px;height:3062px;overflow:hidden}
body{background:var(--backdrop);font-family:"Roboto",Arial,sans-serif;color:var(--text);position:relative}
.page{position:absolute;left:105px;width:990px;height:1400px;background:var(--paper);overflow:hidden;box-shadow:10px 10px 0 rgba(0,0,0,.18)}
.page-front{top:87px}
.page-back{top:1575px}
.abs{position:absolute}

/* brand */
.brand{left:46px;top:52px;display:flex;align-items:center;gap:20px}
.brand-mark{width:86px;height:86px;background:var(--magenta);border:10px solid var(--teal)}
.brand-name{font-family:"Montserrat",sans-serif;font-weight:700;font-size:40px;color:var(--ink);letter-spacing:1px}

/* hero */
.hero{left:0;top:181px;width:467px;height:367px;background:linear-gradient(180deg,var(--magenta) 0%,var(--magenta-dark) 100%);padding:40px 30px 0 46px;color:#fff}
.hero-title{font-family:"Montserrat",sans-serif;font-weight:800;line-height:1}
.hero-title .l1{display:block;font-size:46px}
.hero-title .l2{display:block;font-size:78px;margin-top:4px}
.hero-rule{width:64px;height:3px;background:#fff;opacity:.8;margin:22px 0 16px}
.hero-sub{font-size:23px;line-height:1.22}

.photo-frame{left:467px;top:72px;width:523px;height:554px;background:var(--teal)}
.frame-accent-top{left:826px;top:72px;width:164px;height:40px;background:var(--magenta)}
.frame-accent-bottom{left:826px;top:583px;width:164px;height:43px;background:var(--magenta)}
.photo{left:518px;top:118px;width:472px;height:465px;background:linear-gradient(135deg,#5b4a3a 0%,#3e342c 45%,#8a7a5e 100%)}

/* training formats */
.format{width:230px;text-align:center}
.format svg{display:block;margin:0 auto}
.format-label{font-family:"Roboto Condensed",sans-serif;font-weight:700;font-size:23px;color:var(--ink);line-height:1;margin-top:4px}

/* funding */
.funder-flag{left:46px;top:1190px;width:137px;height:93px;background:#1e3d9a}
.funder-text{left:205px;top:1200px;width:265px;font-size:15px;line-height:1.2;font-weight:500;color:var(--ink)}

/* challenge panel */
.panel{left:518px;top:672px;width:424px;height:623px;background:var(--panel)}
.tab{height:56px;color:#fff;font-family:"Montserrat",sans-serif;font-weight:800;font-size:28px;line-height:56px;padding-left:30px;border-radius:0 28px 28px 0}
.tab-teal{background:var(--teal)}
.tab-magenta{background:var(--magenta)}
.challenge-tab{left:495px;top:709px;width:302px}
.challenge-body{left:570px;top:800px;width:350px}
.lead{font-size:20px;line-height:1.2;color:var(--ink);margin-bottom:28px}
.ticks{list-style:none}
.ticks li{display:flex;gap:14px;font-size:15px;line-height:1.2;margin-bottom:16px}
.ticks li svg{flex:0 0 20px;margin-top:1px}
.need{font-size:15px;margin:30px 0 28px;line-height:1.25}
.need b{font-size:19px;font-weight:500;color:var(--ink)}
.offer{font-size:15px;line-height:1.25}

/* footer front */
.footer-front{left:0;top:1312px;width:990px;height:88px}
.footer-contact{left:46px;top:1322px;color:#fff;font-size:21px;letter-spacing:2.5px;line-height:30px}
.footer-contact span{display:inline-block;width:14px;height:14px;background:var(--teal);margin-right:18px;border-radius:50%}
.social-row{left:340px;top:1358px;display:flex;gap:10px}
.social-row span{display:inline-block;width:19px;height:19px;border:2px solid var(--magenta)}

/* back page */
.photo-back{left:0;top:0;width:990px;height:456px;background:linear-gradient(120deg,#4a4a4a 0%,#9a9a9a 40%,#e0e0e0 60%,#6d6d6d 100%)}
.band-teal{left:0;top:456px;width:635px;height:37px;background:var(--teal)}
.band-magenta{left:635px;top:456px;width:355px;height:37px;background:var(--magenta)}
.offers-tab{left:0;top:519px;width:300px}
.involved-tab{left:497px;top:519px;width:249px}
.list-left{left:35px;top:600px;width:400px}
.list-right{left:497px;top:600px;width:400px}
.ticks.small li{font-size:14px;font-weight:500;color:var(--ink);margin-bottom:14px}
.ticks a,.accent{color:var(--teal);text-decoration:none}
.section-head{font-family:"Montserrat",sans-serif;font-weight:800;font-size:27px;color:var(--teal)}
.section-head::after{content:"";display:block;width:70px;height:3px;background:var(--magenta);margin-top:8px}
.partners-head{left:35px;top:845px}
.partners{left:35px;top:900px;width:400px;display:grid;grid-template-columns:repeat(4,1fr);gap:16px 18px}
.partners span{height:22px;background:#cfd4d8;border-radius:3px}
.partners span.round{width:26px;border-radius:50%}

.contact-box{left:33px;top:1043px;width:462px;height:202px;background:var(--teal);border-radius:0 0 16px 16px}
.contact-tab{left:33px;top:1043px;width:366px;height:74px;background:var(--magenta);border-radius:0 0 14px 0;color:#fff;font-family:"Montserrat",sans-serif;padding:10px 0 0 35px;line-height:1}
.contact-tab b{display:block;font-weight:800;font-size:26px}
.contact-tab i{font-style:normal;font-weight:700;font-size:26px;opacity:.95}
.contact-lines{left:68px;top:1150px;color:#fff;font-size:15px;line-height:42px}
.contact-lines .sq{display:inline-block;width:14px;height:14px;border:2px solid #fff;vertical-align:-2px;margin:0 8px 0 0}
.contact-lines .gap{display:inline-block;width:20px}

.questions{left:35px;top:1262px;width:440px}
.questions h3{font-family:"Montserrat",sans-serif;font-weight:800;font-size:22px;color:var(--magenta);margin-bottom:10px}
.questions p{font-size:14px;font-weight:500;line-height:1.25;color:var(--ink)}

.who-head{left:497px;top:778px}
.audience{width:230px;text-align:center}
.audience h4{font-family:"Roboto Condensed",sans-serif;font-weight:700;font-size:17px;line-height:1.05;color:var(--ink);margin:2px 0 6px}
.audience p{font-size:13.5px;line-height:1.25}
.footer-back{left:0;top:1340px;width:990px;height:60px}
</style>
</head>
<body>

<svg width="0" height="0" style="position:absolute" aria-hidden="true">
  <defs>
    <symbol id="tick" viewBox="0 0 20 20">
      <circle cx="10" cy="10" r="8.5" fill="none" stroke="#14b3c6" stroke-width="1.6"/>
      <path d="M5.8 10.2l3 3 5.6-6.2" fill="none" stroke="#14b3c6" stroke-width="2" stroke-linecap="round" stroke-linejoin="round"/>
    </symbol>
    <symbol id="pin" viewBox="0 0 120 130">
      <circle cx="60" cy="56" r="53" fill="#14b3c6"/>
      <path d="M36 100 L84 100 L60 128 Z" fill="#14b3c6"/>
      <circle cx="60" cy="56" r="41" fill="#ffffff"/>
    </symbol>
  </defs>
</svg>

<!-- FRONT PAGE -->
<section class="page page-front">
  <div class="abs brand"><div class="brand-mark"></div><div class="brand-name">PS Forum</div></div>

  <div class="abs hero">
    <h1 class="hero-title"><span class="l1">Parity Skills</span><span class="l2">Forum</span></h1>
    <div class="hero-rule"></div>
    <p class="hero-sub">A high-quality capacity-building programme on gender equality in research, innovation and higher education</p>
  </div>

  <div class="abs photo-frame"></div>
  <div class="abs frame-accent-top"></div>
  <div class="abs frame-accent-bottom"></div>
  <div class="abs photo" role="img" aria-label="Photo of students reading and taking notes at a wooden table"></div>

  <div class="abs format" style="left:18px;top:590px">
    <svg width="110" height="120" viewBox="0 0 120 130"><use href="#pin"/><rect x="44" y="36" width="32" height="22" fill="none" stroke="#c0245e" stroke-width="4"/><rect x="40" y="64" width="40" height="8" rx="3" fill="#c0245e"/></svg>
    <div class="format-label">In person-trainings</div>
  </div>
  <div class="abs format" style="left:248px;top:590px">
    <svg width="110" height="120" viewBox="0 0 120 130"><use href="#pin"/><rect x="40" y="34" width="40" height="24" rx="2" fill="#14b3c6"/><rect x="38" y="64" width="44" height="8" rx="3" fill="#c0245e"/></svg>
    <div class="format-label">Workshops</div>
  </div>
  <div class="abs format" style="left:18px;top:778px">
    <svg width="110" height="120" viewBox="0 0 120 130"><use href="#pin"/><path d="M40 48 L60 34 L80 48 Z" fill="#c0245e"/><rect x="43" y="50" width="34" height="24" fill="#c0245e"/></svg>
    <div class="format-label">Summer Schools</div>
  </div>
  <div class="abs format" style="left:248px;top:778px">
    <svg width="110" height="120" viewBox="0 0 120 130"><use href="#pin"/><rect x="46" y="34" width="28" height="40" rx="2" fill="#c0245e"/><rect x="51" y="50" width="18" height="3" fill="#fff"/><rect x="51" y="57" width="18" height="3" fill="#fff"/></svg>
    <div class="format-label">Webinars</div>
  </div>
  <div class="abs format" style="left:18px;top:972px">
    <svg width="110" height="120" viewBox="0 0 120 130"><use href="#pin"/><rect x="44" y="34" width="32" height="22" rx="2" fill="#c0245e"/><rect x="40" y="62" width="40" height="10" rx="4" fill="#c0245e"/></svg>
    <div class="format-label">DOCCs</div>
  </div>
  <div class="abs format" style="left:248px;top:972px">
    <svg width="110" height="120" viewBox="0 0 120 130"><use href="#pin"/><rect x="40" y="38" width="30" height="22" rx="2" fill="#c0245e"/><circle cx="74" cy="40" r="7" fill="none" stroke="#c0245e" stroke-width="3"/><rect x="40" y="64" width="40" height="8" rx="3" fill="#c0245e"/></svg>
    <div class="format-label">Train-the<br>Trainers sessions</div>
  </div>

  <div class="abs funder-flag" role="img" aria-label="Funder banner"></div>
  <p class="abs funder-text">This project has received funding from the Union Vexa's Horizon Nova research and innovation programme under grant agreement No 731206</p>

  <div class="abs panel"></div>
  <div class="abs tab tab-teal challenge-tab">The challenge</div>
  <div class="abs challenge-body">
    <p class="lead">Currently, there are many programmes, projects and a great gained knowledge and experience, BUT</p>
    <ul class="ticks">
      <li><svg width="20" height="20"><use href="#tick"/></svg>Gender analysis remains rarely appropriated within research projects</li>
      <li><svg width="20" height="20"><use href="#tick"/></svg>Large differences among research performing organisations in various countries</li>
      <li><svg width="20" height="20"><use href="#tick"/></svg>Small proportion of researchers and practitioners are familiar with theoretical and methodological concepts of gender and feminist scholarship</li>
    </ul>
    <p class="need"><b>Need:</b> A holistic approach to structural change for gender equality in R&amp;I</p>
    <p class="offer">The Parity Skills Forum project offers high-quality capacity-building programme on gender equality in research, innovation and higher education</p>
  </div>

  <svg class="abs footer-front" viewBox="0 0 990 88" preserveAspectRatio="none" aria-hidden="true">
    <path d="M0 0 H410 C440 0 440 26 470 26 H990 V88 H0 Z" fill="#30363b"/>
    <path d="M470 20 H990" stroke="#c0245e" stroke-width="10"/>
  </svg>
  <div class="abs footer-contact"><div><span></span>www.ps-forum.eu</div><div><span></span>info@ps-forum.eu</div></div>
  <div class="abs social-row"><span></span><span></span><span></span></div>
</section>

<!-- BACK PAGE -->
<section class="page page-back">
  <div class="abs photo-back" role="img" aria-label="Black and white photo of a group of people laughing around a meeting table"></div>
  <div class="abs band-teal"></div>
  <div class="abs band-magenta"></div>

  <div class="abs tab tab-magenta offers-tab">Training offers</div>
  <div class="abs tab tab-magenta involved-tab">Get involved</div>

  <ul class="abs ticks small list-left">
    <li><svg width="20" height="20"><use href="#tick"/></svg>Trainings are offered for free to those interested to understand and consider gender equality and dimension as an integral part of research and innovation.</li>
    <li><svg width="20" height="20"><use href="#tick"/></svg><span>Find the offer which suits you best and register on <a href="#">https://ps-forum.eu/</a></span></li>
    <li><svg width="20" height="20"><use href="#tick"/></svg>There are different dates and locations</li>
    <li><svg width="20" height="20"><use href="#tick"/></svg><span>Course Language: <span class="accent">English</span></span></li>
    <li><svg width="20" height="20"><use href="#tick"/></svg>Participation is free thanks to the UVC.</li>
  </ul>

  <ul class="abs ticks small list-right">
    <li><svg width="20" height="20"><use href="#tick"/></svg>Take part in one or more offered trainings Become a gender trainer</li>
    <li><svg width="20" height="20"><use href="#tick"/></svg>Become a host institution to the topic of your preference</li>
    <li><svg width="20" height="20"><use href="#tick"/></svg>Be part of the pan European gender trainers' network</li>
  </ul>

  <h2 class="abs section-head partners-head">Partners</h2>
  <div class="abs partners" role="img" aria-label="Partner organisation badges">
    <span></span><span></span><span></span><span></span>
    <span></span><span></span><span></span><span></span>
    <span></span><span class="round"></span><span></span><span></span>
  </div>

  <div class="abs contact-box"></div>
  <div class="abs contact-tab"><b>Got your attention?</b><i>Stay in touch!</i></div>
  <div class="abs contact-lines">
    <div><span class="sq"></span>@PSForum_eu<span class="gap"></span><span class="sq"></span>@PSForum.eu<span class="gap"></span><span class="sq"></span>PS Forum</div>
    <div><span class="sq"></span>www.ps-forum.eu<span class="gap"></span><span class="sq"></span>info@ps-forum.eu</div>
  </div>

  <div class="abs questions">
    <h3>Do you still have questions?</h3>
    <p>Feel free to contact us at info@ps-forum.eu<br>A member of the team will make her/his best to reply as soon as possible.</p>
  </div>

  <h2 class="abs section-head who-head">Who is it for?</h2>

  <div class="abs audience" style="left:497px;top:840px">
    <svg width="68" height="74" viewBox="0 0 120 130"><use href="#pin"/><rect x="48" y="36" width="24" height="34" rx="3" fill="#c0245e"/></svg>
    <h4>HR Professionals</h4>
    <p>Integration and establishment of gender-sensitive and fair recruitment and career management processes in organisation</p>
  </div>
  <div class="abs audience" style="left:740px;top:840px">
    <svg width="68" height="74" viewBox="0 0 120 130"><use href="#pin"/><rect x="42" y="36" width="36" height="22" fill="none" stroke="#c0245e" stroke-width="4"/><rect x="44" y="62" width="32" height="8" rx="3" fill="#c0245e"/></svg>
    <h4>Gender Trainers<br>&amp; Experts</h4>
    <p>Train-the-trainers sessions for the development of new skills</p>
  </div>
  <div class="abs audience" style="left:497px;top:1073px">
    <svg width="68" height="74" viewBox="0 0 120 130"><use href="#pin"/><circle cx="60" cy="48" r="14" fill="none" stroke="#c0245e" stroke-width="4"/><rect x="44" y="64" width="32" height="8" rx="3" fill="#c0245e"/></svg>
    <h4>Researchers</h4>
    <p>Training to integrate the gender dimension in their research and deepening their understanding of gender issues in R&amp;I</p>
  </div>
  <div class="abs audience" style="left:740px;top:1073px">
    <svg width="68" height="74" viewBox="0 0 120 130"><use href="#pin"/><rect x="44" y="34" width="32" height="40" rx="2" fill="#c0245e"/><rect x="49" y="44" width="22" height="3" fill="#fff"/><rect x="49" y="52" width="22" height="3" fill="#fff"/><rect x="49" y="60" width="22" height="3" fill="#fff"/></svg>
    <h4>Research Performing<br>Organisations</h4>
    <p>Recommendations for influencing the internal policies and practices of the organisations towards gender equality</p>
  </div>

  <svg class="abs footer-back" viewBox="0 0 990 60" preserveAspectRatio="none" aria-hidden="true">
    <path d="M0 30 H520 C550 30 560 22 570 14 H990 V60 H0 Z" fill="#c0245e"/>
    <path d="M0 40 H540 C565 40 575 24 590 22 H990 V60 H0 Z" fill="#30363b"/>
  </svg>
</section>

</body>
</html>
```